Update Law Firm Website

Update law firm website pages, add pages for employees. Current website looks stale. www.lowrevanlaw.com

Target Market(s)

Personal injury clients

Industry/Entity Type

Legal

Number of Pages Required

5+ page

Font styles to use
Serif

Requirements
Must have
• User friendly and engaging design
Nice to have
• ?
Should not have
• scales of justice, law books,

```html
<!DOCTYPE html>
<html lang="en">
<head>
<meta charset="utf-8">
<title>Larkfield Law</title>
<link href="https://fonts.googleapis.com/css2?family=Open+Sans:ital,wght@0,400;0,600;0,700;1,400;1,700&family=Bitter:wght@700&family=Arimo:ital,wght@0,400;0,700;1,400&display=swap" rel="stylesheet">
<style>
:root{
  --purple:#5b54a6;
  --purple-text:#6a62b0;
  --ink:#333;
  --muted:#777;
  --soft:#999;
  --panel:#efefef;
  --rule:#e2e2e2;
  --white:#fff;
}
*{margin:0;padding:0;box-sizing:border-box}
html,body{width:932px;height:1200px;overflow:hidden;background:var(--white)}
body{position:relative;font-family:"Arimo",Arial,sans-serif;color:var(--ink)}
.abs{position:absolute}

.topbar{left:416px;top:0;width:436px;height:21px;background:#f0f0f0;font-size:8px;color:#444}
.topbar .welcome{left:21px;top:6px}
.topbar .social{left:140px;top:7px;display:flex;gap:8px}
.topbar .social span{width:6px;height:6px;border-radius:50%;background:#555;display:block}
.topbar .phone{left:340px;top:6px;display:flex;gap:5px;align-items:center}

.brand{left:70px;top:26px;display:flex;align-items:center;gap:10px}
.brand .dot{width:22px;height:22px;border-radius:50%;background:var(--purple)}
.brand .name{font-family:"Open Sans",sans-serif;font-size:31px;font-weight:400;color:var(--purple-text);letter-spacing:1.5px}

.nav{top:43px;left:437px;font-family:"Open Sans",sans-serif;font-size:14.5px;color:#8a8a8a;letter-spacing:.6px}
.nav a{position:absolute;top:0;white-space:nowrap;color:inherit;text-decoration:none}
.nav a.current{color:var(--purple);font-weight:600}

.hero{left:0;top:91px;width:932px;height:267px;background:linear-gradient(90deg,#f4f4f4 0%,#e9e9e9 45%,#dcdcdc 100%)}
.hero-photo{left:446px;top:0;width:486px;height:267px;background:linear-gradient(180deg,#e6e6e6 0%,#d9d9d9 50%,#cfcfcf 100%)}
.hero h1{left:94px;top:106px;font-family:"Open Sans",sans-serif;font-weight:400;font-size:23px;color:#4a4a4a;letter-spacing:-.3px}
.hero p{left:95px;top:141px;width:290px;font-size:9.6px;line-height:14.4px;color:#333}

.band{left:0;top:358px;width:932px;height:119px;background:var(--purple);color:var(--white)}
.feature{top:24px;width:200px}
.feature h3{font-family:"Bitter",serif;font-size:14.5px;font-weight:700;display:flex;align-items:center;gap:11px;height:22px}
.feature p{margin-top:12px;font-size:7.4px;line-height:12.8px}

.quote{left:144px;top:498px;width:688px;height:70px;background:#f2f2f2;border-left:3px solid #444}
.quote .avatar{left:21px;top:10px;width:48px;height:48px;border-radius:50%;background:radial-gradient(circle at 50% 40%,#e9d7c6,#cdb9a8);border:2px solid var(--white);box-shadow:0 1px 3px rgba(0,0,0,.2)}
.quote blockquote{left:83px;top:13px;width:590px;font-style:italic;font-size:9.6px;line-height:16.8px;color:#666}
.quote .by{left:595px;top:49px;font-family:"Open Sans",sans-serif;font-size:8.5px;color:#666;font-style:italic}
.quote .by b{color:#333}
.quote .arrows{left:652px;top:48px;font-size:11px;color:#333;letter-spacing:4px}

.expertise{left:149px;top:576px;width:150px}
.expertise h2{font-family:"Open Sans",sans-serif;font-style:italic;font-weight:700;font-size:17.5px;color:#222;padding-left:2px;padding-bottom:7px;border-bottom:3px solid var(--rule)}
.expertise ul{list-style:none}
.expertise li{display:flex;align-items:center;gap:6px;height:26px;border-bottom:1px dashed var(--rule);font-size:8.8px;color:var(--muted)}
.expertise li .plus{width:12px;height:12px;border-radius:50%;background:#2c2c2c;position:relative;flex:none}
.expertise li .plus::before,.expertise li .plus::after{content:"";position:absolute;background:var(--white);left:3px;top:5.3px;width:6px;height:1.4px}
.expertise li .plus::after{transform:rotate(90deg)}

.profile{left:320px;top:577px;width:314px}
.profile h2{font-family:"Open Sans",sans-serif;font-style:italic;font-weight:700;font-size:21px;color:#6f6f6f}
.profile p{font-size:8.8px;line-height:17.6px;color:var(--muted);margin-bottom:17.6px}
.profile p.tight{margin-bottom:0}
.profile p.after{margin-top:17.6px}

.courthouse{left:645px;top:582px;width:176px;height:233px;background:linear-gradient(180deg,#6d9bd6 0%,#a9c3e3 30%,#c9b58e 55%,#9a8a70 80%,#5a5a5a 100%)}

.lower{left:0;top:878px;width:932px;height:248px;background:var(--panel);border-top:2px solid #e6e6e6}
.lower h4{position:absolute;top:36px;font-family:"Bitter",serif;font-size:11px;font-weight:700;color:#444;letter-spacing:-.2px}
.map{left:145px;top:66px;width:228px;height:150px;border:3px solid var(--white);box-shadow:0 1px 3px rgba(0,0,0,.15);background:linear-gradient(135deg,#ece6dc,#e3dcd0)}
.advice{left:404px;width:270px}
.advice .thumb{left:0;top:0;width:67px;height:67px;border:3px solid var(--white);box-shadow:0 1px 3px rgba(0,0,0,.15);background:linear-gradient(180deg,#7ea6d9 0%,#c7b48e 60%,#6c6458 100%)}
.advice h5{left:76px;top:3px;font-family:"Bitter",serif;font-size:10.4px;color:#444;white-space:nowrap}
.advice p{left:77px;top:18px;width:180px;font-size:7.2px;line-height:11.2px;color:var(--muted)}
.field{left:696px;width:136px;background:var(--white);font-size:8px;font-style:italic;color:#999;padding:7px 8px}
.send{left:764px;top:194px;width:68px;height:22px;background:#3d3d3d;color:var(--white);font-size:9px;text-align:center;line-height:22px}

.footer{left:0;top:1126px;width:932px;height:74px;font-size:8.8px;color:#222}
.footer span{position:absolute;top:23px;white-space:nowrap}
</style>
</head>
<body>

<div class="abs topbar">
  <span class="abs welcome">Welcome to our website</span>
  <div class="abs social"><span></span><span></span><span></span><span></span></div>
  <span class="abs phone">
    <svg width="8" height="8" viewBox="0 0 24 24"><path fill="#333" d="M6.6 10.8a15.1 15.1 0 0 0 6.6 6.6l2.2-2.2c.3-.3.7-.4 1-.2 1.1.4 2.3.6 3.6.6.6 0 1 .4 1 1V20c0 .6-.4 1-1 1A17 17 0 0 1 3 4c0-.6.4-1 1-1h3.5c.6 0 1 .4 1 1 0 1.3.2 2.5.6 3.6.1.3 0 .7-.2 1z"/></svg>
    0100 555 0142
  </span>
</div>

<div class="abs brand">
  <span class="dot"></span>
  <span class="name">Larkfield Law</span>
</div>

<nav class="abs nav">
  <a class="current" style="left:0">Home</a>
  <a style="left:65px">About us</a>
  <a style="left:160px">Services</a>
  <a style="left:249px">Apeal</a>
  <a style="left:319px">Contact Us</a>
</nav>

<section class="abs hero">
  <div class="abs hero-photo" role="img" aria-label="Photo of three lawyers in business suits standing together"></div>
  <h1 class="abs">FOR THE SERVICE YOU DESERVE</h1>
  <p class="abs">Lorem ipsum dolor sit amet, consectetur adipisicing elit, sed do eiusmod tempor incididunt..</p>
</section>

<section class="abs band">
  <div class="abs feature" style="left:144px">
    <h3><svg width="24" height="19" viewBox="0 0 24 19"><rect x="8" y="0.5" width="8" height="4" rx="1" fill="none" stroke="#fff" stroke-width="1.6"/><rect x="0" y="4" width="24" height="15" rx="2" fill="#fff"/><rect x="0" y="10" width="24" height="1.4" fill="#5b54a6"/></svg>Solid Law Practice</h3>
    <p>Lorem ipsum dolor sit amet, consectetur adipisicing elit, sed do eiusmod tempor incididunt ut labore et dolore magna aliqua.</p>
  </div>
  <div class="abs feature" style="left:372px">
    <h3><svg width="15" height="20" viewBox="0 0 15 20"><path d="M7.5 1.5a5.8 5.8 0 0 0-3.3 10.6c.6.5.9 1.1.9 1.8V15h4.8v-1.1c0-.7.3-1.3.9-1.8A5.8 5.8 0 0 0 7.5 1.5z" fill="none" stroke="#fff" stroke-width="1.8"/><rect x="5" y="16.5" width="5" height="2.2" rx="1" fill="#fff"/></svg>Creative Thinking</h3>
    <p>Lorem ipsum dolor sit amet, consectetur adipisicing elit, sed do eiusmod tempor incididunt ut labore et dolore magna aliqua.</p>
  </div>
  <div class="abs feature" style="left:601px">
    <h3><svg width="20" height="20" viewBox="0 0 20 20"><path d="M5 1h10v5a5 5 0 0 1-10 0z" fill="#fff"/><path d="M5 3H1.5v2A3.5 3.5 0 0 0 5 8.5M15 3h3.5v2A3.5 3.5 0 0 1 15 8.5" fill="none" stroke="#fff" stroke-width="1.5"/><rect x="9" y="11" width="2" height="4" fill="#fff"/><rect x="5" y="15" width="10" height="3.5" rx="1" fill="#fff"/></svg>Award Winning Company</h3>
    <p>Lorem ipsum dolor sit amet, consectetur adipisicing elit, sed do eiusmod tempor incididunt ut labore et dolore magna aliqua.</p>
  </div>
</section>

<section class="abs quote">
  <div class="abs avatar" role="img" aria-label="Portrait photo of the client giving the testimonial"></div>
  <blockquote class="abs">Ut enim ad minim veniam, quis nostrud exercitation ullamco laboris nisi ut aliquip ex ea commodo consequat. Duis aute irure dolor in reprehenderit in voluptate velit esse cillum dolore.</blockquote>
  <span class="abs by">by <b>Nora Pell</b></span>
  <span class="abs arrows">‹›</span>
</section>

<aside class="abs expertise">
  <h2>Area of Expertise</h2>
  <ul>
    <li><span class="plus"></span>Lorem ipsum dolor</li>
    <li><span class="plus"></span>Sit amet</li>
    <li><span class="plus"></span>Adipisicing elit</li>
    <li><span class="plus"></span>Excepteur sint occaecat</li>
  </ul>
</aside>

<article class="abs profile">
  <h2>Daniel Marsh</h2>
  <p>Daniel Marsh qualified as a solicitor in 1987 and spent many years working with a busy commercial practice in North Eastbury.</p>
  <p>He qualified in the city centre where he worked for many years and then set up his own firm in 1981 and then going on to join a larger commercial practice for 2 years.</p>
  <p class="tight">MARSH and HOLT is a firm of solicitors with offices in Riverside, Eastbury and Oakmere, Westshire. This firm is authorised and regulated by the Legal Standards Board, no.480219.</p>
  <p class="tight">VAT registered number: 731 2206 48</p>
  <p class="after">Professional rules can be viewed on www.lsb-example.org/conduct.</p>
</article>

<div class="abs courthouse" role="img" aria-label="Photo of a gothic stone court building under blue sky"></div>

<section class="abs lower">
  <h4 style="left:144px">FIND OUR OFFICE</h4>
  <h4 style="left:404px">ADVICES &amp; BEST PRACTICES</h4>
  <h4 style="left:695px">QUICK CONTACT</h4>

  <div class="abs map" role="img" aria-label="Street map showing the office location"></div>

  <div class="abs advice" style="top:65px">
    <div class="abs thumb" role="img" aria-label="Photo of a court building"></div>
    <h5 class="abs">Strategies for your Success</h5>
    <p class="abs">Lorem ipsum dolor sit amet, consectetur elit, sed do eiusmod tempor. Officia deserunt mollit anim id est laborum reprehenderit in voluptate. sint occaecat cupidatat.</p>
  </div>
  <div class="abs advice" style="top:150px">
    <div class="abs thumb" role="img" aria-label="Photo of a court building"></div>
    <h5 class="abs">Strategies for your Success</h5>
    <p class="abs">Lorem ipsum dolor sit amet, consectetur elit, sed do eiusmod tempor. Officia deserunt mollit anim id est laborum reprehenderit in voluptate. sint occaecat cupidatat.</p>
  </div>

  <div class="abs field" style="top:66px;height:20px;padding-top:6px">Email</div>
  <div class="abs field" style="top:96px;height:20px;padding-top:6px">Subject</div>
  <div class="abs field" style="top:124px;height:56px">Text</div>
  <div class="abs send">Send</div>
</section>

<footer class="abs footer">
  <span style="left:145px">© 2012 Copyright</span>
  <span style="left:286px">LEGAL NOTICES | PRIVACY POLICY</span>
  <span style="left:566px">Home</span>
  <span style="left:607px">Area of Expertise</span>
  <span style="left:691px">news</span>
  <span style="left:730px">Contact</span>
</footer>

</body>
</html>
```